Hi,

I am in desperate need of Wordpress website template for for my consulting company. All the graphics are already there, but I need someone who can code that into an extremely nice template for Wordpress (latest version 3.8.1)

I specialize in Consulting and Advise on global software delivery, with a special focus on how to secure innovation within the global delivery platform. I do have the logo and visual identity.

```html
<!DOCTYPE html>
<html lang="en">
<head>
<meta charset="utf-8">
<title>Novantra — Global Software Delivery Consulting</title>
<link rel="stylesheet" href="https://fonts.googleapis.com/css2?family=Source+Sans+3:wght@400;600&display=swap">
<style>
:root{
  --accent:#3bb6dd;
  --accent-dark:#2a9fc4;
  --link:#4a8fd0;
  --ink:#2d2d2d;
  --text:#555;
  --muted:#777;
  --line:#d8d8d8;
  --band:#f4f4f4;
  --footer:#3a3b3e;
  --footer-text:#d6d6d6;
  --dark-btn:#2b2b2b;
}
*{margin:0;padding:0;box-sizing:border-box}
html,body{width:1177px;height:1200px;overflow:hidden;background:#fff}
body{font-family:"Source Sans 3",sans-serif;color:var(--text);position:relative}
.abs{position:absolute}
.top-strip{left:0;top:0;width:1177px;height:6px;background:var(--accent)}
.site-header{left:0;top:6px;width:1177px;height:115px;border-bottom:1px solid var(--line)}
.brand{left:206px;top:34px;display:flex;align-items:center;gap:12px}
.brand-mark{width:52px;height:52px;border-radius:50%;background:var(--accent-dark)}
.brand-name{font-size:24px;font-weight:600;color:#4a4a4a;letter-spacing:1px}
.phone{right:215px;top:25px;display:flex;align-items:center;gap:6px;font-size:14px;color:var(--ink)}
.follow{right:215px;top:46px;display:flex;align-items:center;gap:3px;font-size:11px;color:var(--ink)}
.follow span{margin-right:4px}
.social{width:19px;height:20px;background:var(--dark-btn)}
.main-nav{right:215px;top:80px;display:flex;gap:16px;font-size:15.5px;color:var(--ink);letter-spacing:.3px}
.main-nav .active{color:var(--accent)}
.hero{left:167px;top:121px;width:875px;height:396px;background:linear-gradient(90deg,#d9cfc8 0%,#efe9e5 30%,#e6e3e2 55%,#d6d2d0 100%)}
.hero-arrow{top:290px;width:42px;height:58px;background:var(--dark-btn);display:flex;align-items:center;justify-content:center}
.hero-arrow.prev{left:0}
.hero-arrow.next{right:0;width:39px}
.hero-caption{left:505px;top:306px;width:476px;height:132px;background:rgba(59,182,221,.88);padding:14px 17px 0 18px;color:#fff}
.hero-caption h1{font-weight:400;font-size:22.5px;letter-spacing:.3px;margin-bottom:8px}
.hero-caption p{font-size:10.5px;line-height:12.6px;margin-left:4px}
.hero-dots{left:893px;top:476px;display:flex;gap:5px}
.hero-dots i{width:13px;height:13px;border-radius:50%;border:1.5px solid #555;background:#fff}
.hero-dots i.on{background:var(--accent-dark);box-shadow:inset 0 0 0 2px #fff}
.projects-band{left:0;top:517px;width:1177px;height:235px;background:var(--band)}
.project-card{top:527px;width:241px;height:203px;background:#fff;border:1px solid #cfcfcf;padding:3px}
.project-card .thumb{height:123px}
.project-card h3{font-weight:400;font-size:15px;color:var(--ink);margin:9px 0 4px 10px;letter-spacing:.3px}
.project-card p{font-size:9.5px;line-height:13.5px;margin:0 10px;color:var(--text)}
.section-title{font-weight:400;font-size:16px;color:var(--ink);letter-spacing:.1px}
.body-copy{font-size:10px;line-height:14px;text-align:justify;color:var(--text)}
.read-more{font-size:10px;color:var(--link)}
.news-underline{left:213px;top:969px;width:94px;height:1px;background:#999}
.avatar{border-radius:50%;background:radial-gradient(circle at 50% 40%,#e8ddd4,#b9aca2)}
.news-text{font-size:10.5px;line-height:14px;color:var(--ink)}
.news-date{font-size:10.5px;color:var(--ink)}
.quote-btn{top:941px;width:18px;height:17px;background:#e3e3e3;border:1px solid #cfcfcf;display:flex;align-items:center;justify-content:center}
.quote-text{left:633px;top:990px;width:300px;font-size:10px;line-height:12.7px;color:var(--text)}
.quote-mark{left:612px;top:982px;font-size:22px;color:#999;font-style:italic}
.quote-rule{left:604px;top:1042px;width:347px;height:1px;background:#e2e2e2}
.client-name{left:669px;top:1061px;font-size:10px;font-weight:600;color:var(--ink)}
.client-country{left:669px;top:1074px;font-size:10px;color:var(--text)}
.site-footer{left:0;top:1130px;width:1177px;height:70px;background:var(--footer);color:var(--footer-text)}
.footer-nav{left:224px;top:17px;font-size:10.5px;display:flex;gap:5px}
.copyright{left:223px;top:41px;font-size:10px}
</style>
</head>
<body>
<div class="abs top-strip"></div>

<header class="abs site-header">
  <div class="abs brand" style="top:28px">
    <div class="brand-mark"></div>
    <div class="brand-name">Novantra</div>
  </div>
  <div class="abs phone">
    <svg width="16" height="12" viewBox="0 0 16 12"><path d="M1 3c2-2 12-2 14 0l-1 2h-3V3H5v2H2z" fill="#222"/><rect x="3" y="6" width="10" height="6" rx="1" fill="#222"/></svg>
    555-010-2040
  </div>
  <div class="abs follow"><span>Follow us :</span><i class="social"></i><i class="social"></i><i class="social"></i><i class="social"></i></div>
  <nav class="abs main-nav"><span class="active">HOME</span><span>ABOUT US</span><span>SERVICES</span><span>PROJECTS</span><span>BLOG</span><span>CONTACT US</span></nav>
</header>

<section>
  <div class="abs hero" role="img" aria-label="Photo of a smiling consultant in glasses in front of a team of business people"></div>
  <div class="abs hero-arrow prev"><svg width="14" height="18" viewBox="0 0 14 18"><path d="M11 2L4 9l7 7" stroke="#fff" stroke-width="3.5" fill="none"/></svg></div>
  <div class="abs hero-arrow next"><svg width="14" height="18" viewBox="0 0 14 18"><path d="M3 2l7 7-7 7" stroke="#fff" stroke-width="3.5" fill="none"/></svg></div>
  <div class="abs hero-caption">
    <h1>GLOBAL SOFTWARE DELIVERY</h1>
    <p>Lorem ipsum dolor sit amet, consectetur adipiscing elit. Nunc sodales, nisi sodales pharetra hendrerit, tellus mi pharetra risus, sed porttitor sLorem ipsum dolor sit amet, consectetur adipiscing elit. Nunc sodales, nisi sodales pharetra hendrerit, tellus mi pharetra risus, sed porttitor sLorem ipsum dolor sit amet, consectetur adipiscing elit. Nunc sodales, nisi sodales pharetr</p>
  </div>
  <div class="abs hero-dots"><i></i><i class="on"></i><i></i><i></i></div>
</section>

<section>
  <div class="abs projects-band"></div>
  <article class="abs project-card" style="left:206px">
    <div class="thumb" role="img" aria-label="Illustration of a blue network of nodes around a globe" style="background:linear-gradient(135deg,#f0f3f5,#cfe3ec 50%,#4aa3cf)"></div>
    <h3>PROJECT TITTLE</h3>
    <p>Lorem ipsum dolor sit amet, consectetur adipiscing elit. Nunc sodales, nisi sodales pharetra</p>
  </article>
  <article class="abs project-card" style="left:468px">
    <div class="thumb" role="img" aria-label="Photo of engineers examining computer hardware" style="background:linear-gradient(90deg,#c9c2b8,#dfe4e7 50%,#5a8fbf)"></div>
    <h3>PROJECT TITTLE</h3>
    <p>Lorem ipsum dolor sit amet, consectetur adipiscing elit. Nunc sodales, nisi sodales pharetra</p>
  </article>
  <article class="abs project-card" style="left:729px">
    <div class="thumb" role="img" aria-label="Photo of server racks" style="background:linear-gradient(90deg,#fff 3%,#333 12%,#1c1c1c 60%,#3a3a3a 90%,#fff 97%)"></div>
    <h3 style="margin-top:13px">PROJECT TITTLE</h3>
    <p>Lorem ipsum dolor sit amet, consectetur adipiscing elit. Nunc sodales, nisi sodales pharetra</p>
  </article>
</section>

<section>
  <h2 class="abs section-title" style="left:212px;top:762px">WELCOME TO WEBSITE</h2>
  <p class="abs body-copy" style="left:213px;top:790px;width:379px">Lorem ipsum dolor sit amet, consectetur adipiscing elit. Nunc sodales, nisi sodales pharetra hendrerit, tellus mi pharetra risus, sed porttitor sapien dui sit amet lacus. Duis sit amet lit nec turpis.Lorem ipsum dolor sit amet, consectetur adipiscing elit. Nunc sodales, nisi sodales pharetra hendrerit Lorem Lorem ipsum dolor sit amet, consectetur adipiscing elit. Nunc sodales, nisi sodales pharetra hendrerit, tellus mi pharetra risus, sed porttitor sapien dui sit amet lacus. Duis sit amet lit nec turpis.Lorem ipsum dolor sit amet, consectetur adipiscing elit. Nunc sodales,</p>
  <a class="abs read-more" style="left:525px;top:896px">Read More &gt;&gt;</a>

  <h2 class="abs section-title" style="left:612px;top:762px;letter-spacing:.6px">GLOBAL DELIVERY PLATFORM</h2>
  <p class="abs body-copy" style="left:612px;top:788px;width:173px;line-height:12.5px">Lorem ipsum dolor sit amet, consectetur adipiscing elitLorem ipsum dolor sit amet, consectetur adipiscing elitLorem ipsum dotlor sit amet, consectetur apipsum dotlor sit amet, consectetur ap ipsum dotlor sit amet, consectetur ap</p>
  <div class="abs" role="img" aria-label="Illustration of two laptops connected around a globe" style="left:792px;top:788px;width:156px;height:80px;background:radial-gradient(ellipse at 50% 60%,#4a9ad6,#c9dff0 55%,#fff 75%)"></div>
  <p class="abs body-copy" style="left:613px;top:869px;width:311px;line-height:12.5px">Lorem ipsum dolor sit amet, consectetur adipiscing elitLorem ipsum dolor sit amet, consectetur adipiscing elitLorem ipsum dotlor sit amet, consectetur ap</p>
  <a class="abs read-more" style="left:881px;top:896px">Read More &gt;&gt;</a>
</section>

<section>
  <h2 class="abs section-title" style="left:213px;top:940px">LATEST NEWS</h2>
  <div class="abs news-underline"></div>
  <div class="abs avatar" role="img" aria-label="Portrait of a news author" style="left:214px;top:982px;width:53px;height:53px"></div>
  <p class="abs news-text" style="left:286px;top:983px">Lorem ipsum dolor sit amet, consectetur adipiscing<br>elitLorem ipsum dolor sit amet, consectetur adipiscing elit</p>
  <p class="abs news-date" style="left:286px;top:1017px">15 Feb, 2014</p>
  <div class="abs avatar" role="img" aria-label="Portrait of a news author" style="left:216px;top:1056px;width:53px;height:53px"></div>
  <p class="abs news-text" style="left:286px;top:1059px">Lorem ipsum dolor sit amet, consectetur adipiscing<br>elitLorem ipsum dolor sit amet, consectetur adipiscing</p>
  <p class="abs news-date" style="left:286px;top:1093px">15 Feb, 2014</p>

  <h2 class="abs section-title" style="left:614px;top:941px">WHAT OUR CUSTOMERS SAY</h2>
  <div class="abs quote-btn" style="left:910px"><svg width="6" height="8" viewBox="0 0 6 8"><path d="M5 1L2 4l3 3" stroke="#333" stroke-width="1.4" fill="none"/></svg></div>
  <div class="abs quote-btn" style="left:933px"><svg width="6" height="8" viewBox="0 0 6 8"><path d="M1 1l3 3-3 3" stroke="#333" stroke-width="1.4" fill="none"/></svg></div>
  <div class="abs quote-mark">&#8220;</div>
  <p class="abs quote-text">Lorem ipsum dolor sit amet, consectetur adipiscing elit. Nunc sodales, nisi sodales pharetra hendrerit, tellus Lorem ipsum dolor sit amet, consectetur adipiscing elit. Nunc sodales, nisi sodales</p>
  <div class="abs quote-rule"></div>
  <div class="abs avatar" role="img" aria-label="Portrait of the customer" style="left:612px;top:1052px;width:44px;height:44px"></div>
  <p class="abs client-name">Name</p>
  <p class="abs client-country">Country</p>
</section>

<footer class="abs site-footer">
  <nav class="abs footer-nav"><span>Home</span>|<span>About us</span>|<span>Services</span>|<span>Projects</span>|<span>Blog</span>|<span>Contact us</span></nav>
  <p class="abs copyright">© 2014, All Rights Reserved</p>
</footer>
</body>
</html>
```